Promotional poster for a vintage motorcycle show.

Vertically oriented, based on 11 x 17 inch proportions

Though not to the exclusion of other design concepts, stylistically perhaps something evoking a vintage (early-mid 20th century) 2-3 color silk screen style event poster.

In addition to some sort of eyecatching, vintage / antique motorbike oriented graphic (preferably not Corwin Baxley based), the poster should include the following text and info:

3rd Annual Milo Quenby Vintage Motorcycle Show
Hallowmere City, N.J.
October 1st (rain date Oct. 2nd)
11am-4pm

Presented in conjunction with the 27th Annual Thistlewood Fair

For further info, or to register your pre-1992 bike contact:
Marty@wheelvaultex.com or 555-204-8913

Sponsored by:
UptownHallowmereGuildway.com
Wheelvaultex.com

Must have
• See above project description
Nice to have
• See above project describtion

```html
<!DOCTYPE html>
<html lang="en">
<head>
<meta charset="utf-8">
<title>3rd Annual Milo Quenby Vintage Motorcycle Show</title>
<link rel="stylesheet" href="https://fonts.googleapis.com/css2?family=Poiret+One&display=swap">
<style>
  :root {
    --ink: #000000;
    --type: #a8a8a8;
    --type-soft: #9c9c9c;
    --rule: #ffffff;
    --art-light: #cfcfcf;
    --art-dark: #5a5a5a;
  }
  html, body {
    margin: 0;
    padding: 0;
    width: 779px;
    height: 1200px;
    overflow: hidden;
    background: var(--ink);
  }
  .poster {
    position: relative;
    width: 779px;
    height: 1200px;
    background: var(--ink);
    overflow: hidden;
  }
  .poster__layout {
    position: absolute;
    inset: 0;
    display: block;
  }
  .poster__type {
    font-family: "Poiret One", sans-serif;
    font-weight: 400;
    fill: var(--type);
    text-anchor: middle;
  }
  .poster__type--soft { fill: var(--type-soft); }
  .motorcycle-art {
    position: absolute;
    left: 52px;
    top: 684px;
    width: 668px;
    height: 516px;
    border-radius: 120px 220px 0 0;
    background: linear-gradient(160deg, var(--art-light) 0%, #9c9c9c 45%, var(--art-dark) 100%);
  }
</style>
</head>
<body>
<main class="poster">
  <div class="motorcycle-art" role="img" aria-label="Screen-printed style illustration of a vintage motorcycle seen from the front, with round headlamp, handlebars and large front tyre in textured grey"></div>

  <svg class="poster__layout" width="779" height="1200" viewBox="0 0 779 1200">
    <g class="deco-frame" fill="none" stroke="var(--rule)" stroke-width="1.5" aria-hidden="true">
      <path d="M102 56 H30 L20 66 V882"/>
      <path d="M102 61 H33 L25 69 V882"/>
      <path d="M102 66 H36 L30 72 V882"/>
      <path d="M102 71 H39 L35 75 V882"/>
      <path d="M677 56 H749 L759 66 V882"/>
      <path d="M677 61 H746 L754 69 V882"/>
      <path d="M677 66 H743 L749 72 V882"/>
      <path d="M677 71 H740 L744 75 V882"/>
      <path d="M120 414 H232 M120 420 H232 M120 426 H232 M120 432 H232"/>
      <path d="M548 414 H658 M548 420 H658 M548 426 H658 M548 432 H658"/>
    </g>
    <circle class="date-badge" cx="390" cy="422" r="158" fill="var(--ink)" stroke="var(--rule)" stroke-width="4" aria-hidden="true"/>

    <text class="poster__type headline--event" x="390" y="94" font-size="64" textLength="544" lengthAdjust="spacingAndGlyphs">3RD ANNUAL MILO QUENBY</text>
    <text class="poster__type headline--show" x="390" y="188" font-size="70" textLength="626" lengthAdjust="spacingAndGlyphs">VINTAGE MOTORCYCLE SHOW</text>
    <text class="poster__type poster__type--soft headline--place" x="390" y="244" font-size="54" textLength="392" lengthAdjust="spacingAndGlyphs">HALLOWMERE CITY, N.J.</text>

    <text class="poster__type date-badge__day" x="390" y="384" font-size="54" textLength="246" lengthAdjust="spacingAndGlyphs">OCTOBER 1ST</text>
    <text class="poster__type date-badge__rain" x="390" y="438" font-size="46" textLength="280" lengthAdjust="spacingAndGlyphs">(RAIN DATE OCT. 2ND)</text>
    <text class="poster__type date-badge__hours" x="390" y="508" font-size="64" textLength="224" lengthAdjust="spacingAndGlyphs">11AM-4PM</text>

    <text class="poster__type poster__type--soft partner-note" x="390" y="620" font-size="29" textLength="290" lengthAdjust="spacingAndGlyphs">PRESENTED IN CONJUNCTION WITH</text>
    <text class="poster__type poster__type--soft partner-note" x="390" y="648" font-size="29" textLength="336" lengthAdjust="spacingAndGlyphs">THE 27TH ANNUAL THISTLEWOOD FAIR</text>
  </svg>
</main>
</body>
</html>
```